TG - management consultant

Business card - contemporary design

Front info
Thomas Galloway

(Address not necessary)
PO Box 7324
Brookvale, CA 94071

(650) 482-3719
tg@thomasgallo.wy

Twitter: tgq287
Facebook: /Thomas.Galloway
Linkedin: /in/thomasgalloway

Back or Front
www.thomasgalloway.net
Facilitation & coaching, change management, strategic partnerships, business improvement

Target Market(s)

High tech businesses - mostly startups in Silicon Valley

Industry/Entity Type

Business

Font styles to use
Sans Serif

Colors

Designer to choose colors to be used in the design.

```html
<!DOCTYPE html>
<html lang="en">
<head>
<meta charset="utf-8">
<title>Thomas Galloway – Business Card</title>
<link rel="stylesheet" href="https://fonts.googleapis.com/css2?family=Arimo:wght@400&display=swap">
<style>
  :root {
    --bg: #5e554b;
    --card: #ffffff;
    --ink: #1a1a1a;
    --band-grey: #d2d2d2;
    --band-grey-dark: #c4c4c4;
    --accent: #e8651c;
    --tab: #111111;
  }
  * { box-sizing: border-box; margin: 0; padding: 0; }
  html, body { width: 1200px; height: 1000px; overflow: hidden; }
  body {
    background: var(--bg);
    font-family: "Arimo", Arial, sans-serif;
    color: var(--ink);
    position: relative;
  }
  h1, h2 { font-weight: 400; }
  .card {
    position: absolute;
    left: 320px;
    width: 560px;
    height: 320px;
    background: var(--card);
    border-radius: 14px;
    overflow: hidden;
    box-shadow: 0 6px 18px rgba(0,0,0,.35);
  }
  .card--front { top: 140px; }
  .card--back { top: 540px; }
  .card svg.art { position: absolute; inset: 0; }

  /* front */
  .front__name {
    position: absolute; left: 70px; top: 70px;
    font-size: 22px; line-height: 26px; white-space: nowrap;
  }
  .front__rule {
    position: absolute; left: 64px; top: 99px;
    width: 190px; height: 1.5px; background: #444;
  }
  .front__tagline {
    position: absolute; left: 70px; top: 104px; width: 210px;
    text-align: right; font-size: 11.5px; line-height: 12.5px; white-space: nowrap;
  }
  .front__contact {
    position: absolute; left: 55px; top: 205px;
    font-size: 10.5px; line-height: 13px; white-space: nowrap;
  }
  .front__contact p + p { margin-top: 10px; }
  .front__social {
    position: absolute; right: 22px; top: 128px;
    list-style: none; font-size: 10.5px; color: var(--ink);
  }
  .front__social li {
    display: flex; align-items: center; justify-content: flex-end;
    gap: 8px; height: 20px; margin-bottom: 2px; white-space: nowrap;
  }
  .front__social .mark {
    width: 18px; height: 18px; background: var(--tab); border-radius: 2px;
  }

  /* back */
  .back__name {
    position: absolute; left: 0; right: 0; top: 88px;
    text-align: center; font-size: 27px; padding-left: 60px; white-space: nowrap;
  }
  .back__tagline {
    position: absolute; left: 0; right: 0; top: 142px;
    text-align: center; font-size: 11px; white-space: nowrap;
  }
  .back__web {
    position: absolute; left: 0; right: 0; top: 190px;
    text-align: center; font-size: 12px; color: #333; letter-spacing: .3px;
  }
</style>
</head>
<body>

<section class="card card--front" aria-label="Card front">
  <svg class="art" width="560" height="320" viewBox="0 0 560 320" aria-hidden="true">
    <rect class="band-grey" x="0" y="162" width="560" height="133" fill="var(--band-grey)"/>
    <polygon class="band-accent" points="420,112 560,112 560,295 362,295" fill="var(--accent)"/>
    <path class="icon-tab" d="M0 192 H40 V292 Q40 306 26 306 H0 Z" fill="var(--tab)"/>
    <g class="icon icon--pin" fill="none" stroke="var(--accent)" stroke-width="2">
      <rect x="12" y="202" width="16" height="16" rx="2"/>
      <circle cx="20" cy="208" r="3"/>
      <path d="M20 211 V216"/>
    </g>
    <path class="icon icon--phone" d="M11 243 q9 -8 18 0 l-2 3 h-3 v-2 h-8 v2 h-3 z M14 246 h12 l2 6 h-16 z" fill="var(--accent)"/>
    <g class="icon icon--mail" fill="none" stroke="var(--accent)" stroke-width="2">
      <rect x="11" y="264" width="18" height="13"/>
      <path d="M11 264 L20 272 L29 264"/>
    </g>
  </svg>

  <h1 class="front__name">Thomas Galloway</h1>
  <div class="front__rule"></div>
  <p class="front__tagline">Facilitation &amp; coaching,<br>change management,<br>strategic partnerships,<br>business improvement</p>

  <div class="front__contact">
    <p>PO Box 7324<br>Brookvale, CA 94071</p>
    <p>(650) 482-3719</p>
    <p>tg@thomasgallo.wy</p>
  </div>

  <ul class="front__social">
    <li>chirp.net/tgq287 <span class="mark"></span></li>
    <li>circles.net/Thomas.Galloway <span class="mark"></span></li>
    <li>careers.net/in/thomasgalloway <span class="mark"></span></li>
  </ul>
</section>

<section class="card card--back" aria-label="Card back">
  <svg class="art" width="560" height="320" viewBox="0 0 560 320" aria-hidden="true">
    <rect class="stripe-accent" x="0" y="166" width="560" height="6" fill="var(--accent)"/>
    <rect class="band-grey" x="0" y="180" width="560" height="66" fill="var(--band-grey-dark)"/>
  </svg>
  <h2 class="back__name">Thomas Galloway</h2>
  <p class="back__tagline">Facilitation &amp; coaching, change management, strategic partnerships, business improvement</p>
  <p class="back__web">WWW.THOMASGALLOWAY.NET</p>
</section>

</body>
</html>
```